Qasrawin Facilities Management brochure

to design suitable company brochure compatible with company scope work, ee are at Qasrawin handling all soft services such as housekeeping , landscaping, waste mangement and pest control and hard services such as building renovations and MEP maintenance ,,,,,,,,,,,,................nnnñnnnnnnnnnnnnnnnnnnnnnnnnnnnnnnnnnnnnnnmnñmmmmmmmmmmmmmmmmm

Target Market(s)

Saudi Arabia

Industry/Entity Type

Facilities Management

Font styles to use
Serif

Requirements
Must have
• Thems matching facilities management feild
Nice to have
• Innovation
Should not have
• Strangers faces photos

```html
<!DOCTYPE html>
<html lang="en">
<head>
<meta charset="utf-8">
<title>Qasrawin Facilities Management – Brochure Covers</title>
<link rel="stylesheet" href="https://fonts.googleapis.com/css2?family=Ubuntu:wght@400;500;700&display=swap">
<style>
  :root {
    --backdrop: #756c5e;
    --navy: #22527a;
    --navy-deep: #1d4669;
    --orange: #c96a3e;
    --orange-deep: #b9503a;
    --gold: #dba526;
    --gold-light: #e8b52a;
    --sky-top: #1f8fdc;
    --sky-low: #cfe3f2;
    --logo-blue: #254a74;
    --white: #ffffff;
    --badge: #a9bccd;
  }
  html, body {
    margin: 0;
    width: 1200px;
    height: 754px;
    overflow: hidden;
    background: var(--backdrop);
    font-family: "Ubuntu", sans-serif;
  }
  .spread {
    position: relative;
    width: 1200px;
    height: 754px;
    display: flex;
    align-items: center;
    justify-content: center;
    gap: 40px;
  }
  .cover {
    width: 540px;
    height: 382px;
    box-shadow: 0 10px 24px rgba(0,0,0,0.35);
    display: block;
  }
  .brand-name { font-family: "Ubuntu", sans-serif; font-weight: 500; }
  .slogan { font-family: "Ubuntu", sans-serif; font-weight: 700; }
  .contact { font-family: "Ubuntu", sans-serif; }
</style>
</head>
<body>
<main class="spread">

  <!-- Front cover -->
  <svg class="cover cover-front" viewBox="0 0 560 396" xmlns="http://www.w3.org/2000/svg">
    <defs>
      <linearGradient id="sky" x1="0" y1="0" x2="0" y2="1">
        <stop offset="0" stop-color="var(--sky-top)"/>
        <stop offset="0.6" stop-color="var(--sky-low)"/>
        <stop offset="1" stop-color="#3a6fa6"/>
      </linearGradient>
      <linearGradient id="goldBand" x1="0" y1="0" x2="1" y2="1">
        <stop offset="0" stop-color="var(--gold-light)"/>
        <stop offset="1" stop-color="var(--gold)"/>
      </linearGradient>
    </defs>
    <rect class="cover-base" width="560" height="396" fill="var(--navy)"/>
    <path class="swoosh-orange" d="M118,0 C30,70 40,160 160,210 L500,396 L560,396 L560,0 Z" fill="var(--orange)"/>
    <path class="swoosh-gold" d="M150,0 C92,70 100,150 205,205 L560,372 L560,0 Z" fill="url(#goldBand)"/>
    <path class="cover-photo" role="img" aria-label="Photograph of the company headquarters building under a blue sky"
          d="M176,0 C122,70 132,140 240,195 L560,335 L560,0 Z" fill="url(#sky)"/>
    <g class="brand-mark">
      <circle cx="326" cy="62" r="9" fill="var(--orange)"/>
      <text class="brand-name" x="342" y="70" font-size="24" fill="var(--logo-blue)">Qasrawin</text>
    </g>
    <text class="slogan" x="440" y="215" font-size="17" fill="var(--gold-light)" text-anchor="middle">Your success</text>
    <text class="slogan" x="440" y="232" font-size="12" fill="var(--gold-light)" text-anchor="middle">is our primary</text>
    <text class="slogan" x="440" y="256" font-size="24" fill="var(--gold-light)" text-anchor="middle">GOAL.</text>
    <text class="contact" x="548" y="320" font-size="11" font-weight="700" fill="var(--white)" text-anchor="end">www.qasrawin-fm.com</text>
    <rect class="partner-badge" x="100" y="312" width="70" height="34" rx="6" fill="var(--badge)" opacity="0.6"/>
  </svg>

  <!-- Back cover -->
  <svg class="cover cover-back" viewBox="0 0 560 396" xmlns="http://www.w3.org/2000/svg">
    <defs>
      <linearGradient id="goldBack" x1="0" y1="0" x2="0" y2="1">
        <stop offset="0" stop-color="var(--gold)"/>
        <stop offset="1" stop-color="var(--gold-light)"/>
      </linearGradient>
    </defs>
    <rect class="cover-base" width="560" height="396" fill="var(--navy)"/>
    <path class="swoosh-orange" d="M110,0 L300,0 L370,60 C420,105 438,190 418,396 L336,396 C336,260 306,190 240,150 Z" fill="var(--orange)"/>
    <path class="swoosh-gold" d="M215,0 L300,0 L370,60 C420,105 438,190 418,396 L388,396 C398,230 368,150 300,110 Z" fill="url(#goldBack)"/>
    <rect class="partner-badge" x="450" y="140" width="70" height="34" rx="6" fill="var(--badge)" opacity="0.6"/>
    <g class="brand-mark">
      <circle cx="50" cy="226" r="8" fill="var(--orange)"/>
      <text class="brand-name" x="64" y="233" font-size="22" fill="var(--white)">Qasrawin</text>
    </g>
    <g class="contact" font-size="9.5" fill="var(--white)">
      <text x="42" y="258" font-weight="700" fill="var(--gold-light)">Address &amp; Office :</text>
      <text x="42" y="272">Qasrawin Sons Trading Company (L.L.C)</text>
      <text x="42" y="285">Al Noor Street, Harbour Road,</text>
      <text x="42" y="298">Al Khobar, Eastern Province,</text>
      <text x="42" y="311">Kingdom of Saudi Arabia</text>
    </g>
    <g class="contact-list contact" font-size="9.5" fill="var(--white)">
      <path class="icon-phone" d="M44,325 q2,-2 4,0 l1,3 q-1,2 1,4 q2,2 4,1 l3,1 q2,2 0,4 q-6,2 -11,-4 q-4,-5 -2,-9 Z" fill="var(--orange)"/>
      <text x="64" y="334">+966 3 812 4470</text>
      <rect class="icon-mail" x="44" y="343" width="12" height="8" fill="var(--gold-light)"/>
      <path d="M44,343 L50,348 L56,343" stroke="var(--navy)" stroke-width="1" fill="none"/>
      <text x="64" y="351">info@qasrawin-fm.com</text>
      <circle class="icon-web" cx="50" cy="364" r="5.5" fill="var(--orange-deep)"/>
      <text x="64" y="368">www.qasrawin-fm.com</text>
    </g>
  </svg>

</main>
</body>
</html>
```